Business card design for immigration consulting business

We need business card design for a company called T&R Migration Advisors Inc. This is a boutique immigration consulting and foreign recruitment agency owned and managed by two partners.
The business card will be used by partners \ owners of the business. The best way to describe the business would be committed to client, passionate about providing top-notch services, engaging, competent, professional

Target Market(s)

We work with individuals in and outside of Canada who need immigration advise as well as Canadian businesses looking to hire or sponsor foreign workers to Canada

Industry/Entity Type

Consulting

Contact Information for Business Card

The business card should have a standard size and horizontal lay-out

Font styles to use
Serif

Colors
f04a50
ec1f27
cbcbcb
dbdbdb

Requirements
Must have
• The business card mush have our logo, name of the company first and last name of the partner, position, phone, cell, fax, e-mail, skype, web-site
• Our first choice would a classic design with minimalist looks and elegant fonts and colors, but we are open minded to any creative ideas too
Nice to have
• On the other side it may have the description of the company: Immigration and Foreign Recruitment Services
• We're considering using stamping \ lettering on our business cards
• It would be nice if the business card would have white space, in case someone would like to make notes on it.
• One (back side) side of the business card can be all red with white logo
Should not have
• We do not want to have our pictures on the business card
• We do no want to have Canadian maple leaf on the business card as we already have one in our logo

```html
<!DOCTYPE html>
<html lang="en">
<head>
<meta charset="utf-8">
<title>T&amp;R Migration Advisors – Business Card</title>
<link rel="stylesheet" href="https://fonts.googleapis.com/css2?family=Cinzel:wght@400;600&family=Open+Sans:wght@400&display=swap">
<style>
  :root {
    --red-deep: #ec1f27;
    --red-soft: #f04a50;
    --grey-light: #dbdbdb;
    --grey-mid: #cbcbcb;
    --card-white: #ececec;
    --text-grey: #6a6a6a;
    --white: #ffffff;
    --backdrop: #f4f4f4;
  }
  * { margin: 0; padding: 0; box-sizing: border-box; }
  html, body {
    width: 1200px; height: 1000px; overflow: hidden;
    background: var(--backdrop);
  }
  .canvas { position: relative; width: 1200px; height: 1000px; }

  .card {
    position: absolute; left: 266px; width: 666px; height: 396px;
    box-shadow: 0 2px 6px rgba(0,0,0,0.18);
  }

  /* Front */
  .card-front { top: 74px; background: var(--red-deep); overflow: hidden; }
  .card-front .pattern-area {
    position: absolute; inset: 0;
    background: linear-gradient(135deg, var(--red-deep), #ee3038 50%, var(--red-deep));
  }
  .card-front .brand-name {
    position: absolute; left: 0; right: 0; top: 168px;
    text-align: center;
    font-family: "Cinzel", serif; font-weight: 600;
    font-size: 58px; letter-spacing: 2px;
    color: var(--white);
  }
  .card-front .tagline {
    position: absolute; left: 0; right: 0; top: 350px;
    text-align: center;
    font-family: "Open Sans", sans-serif; font-size: 16px;
    color: var(--white);
  }

  /* Back */
  .card-back { top: 534px; background: var(--card-white); }
  .person-name {
    position: absolute; left: 32px; top: 78px;
    font-family: "Cinzel", serif; font-weight: 600; font-size: 21px;
    color: var(--red-deep); letter-spacing: 0.5px;
  }
  .person-title {
    position: absolute; left: 32px; top: 105px;
    font-family: "Open Sans", sans-serif; font-size: 16px;
    color: var(--text-grey);
  }
  .contact-list {
    position: absolute; left: 32px; top: 150px; list-style: none;
    font-family: "Open Sans", sans-serif; font-size: 16px; color: var(--text-grey);
  }
  .contact-list li { display: flex; align-items: center; height: 23.5px; }
  .contact-list li.gap-after { margin-bottom: 8px; }
  .contact-list svg { width: 14px; height: 14px; margin-right: 7px; flex: none; }
  .back-mark {
    position: absolute; left: 310px; right: 26px; top: 168px;
    text-align: center;
    font-family: "Cinzel", serif; font-weight: 600; font-size: 44px;
    letter-spacing: 1px; color: var(--grey-mid);
  }
</style>
</head>
<body>
<div class="canvas">

  <section class="card card-front" aria-label="Business card front">
    <div class="pattern-area" role="img" aria-label="Repeating pattern of soft red leaves on red background"></div>
    <div class="brand-name">T&amp;R Migration</div>
    <p class="tagline">Immigration and Foreign Recruitment Services</p>
  </section>

  <section class="card card-back" aria-label="Business card back">
    <h1 class="person-name">Dana Whitfield</h1>
    <p class="person-title">Managing Director</p>
    <ul class="contact-list">
      <li class="gap-after">
        <svg viewBox="0 0 14 14"><circle cx="7" cy="7" r="7" fill="var(--red-deep)"/></svg>trmigration
      </li>
      <li>
        <svg viewBox="0 0 14 14"><rect x="3.5" y="0.5" width="7" height="13" rx="1.2" fill="none" stroke="var(--red-deep)" stroke-width="1.3"/><rect x="5" y="2.5" width="4" height="6" fill="var(--red-deep)"/></svg>+ 000 000 000
      </li>
      <li>
        <svg viewBox="0 0 14 14"><path d="M1 5 Q7 0 13 5 L11 7 L9 5 L5 5 L3 7 Z" fill="var(--red-deep)"/><rect x="3" y="7" width="8" height="6" rx="1" fill="var(--red-deep)"/></svg>+ 000 000 000
      </li>
      <li>
        <svg viewBox="0 0 14 14"><rect x="3.5" y="1" width="7" height="4" fill="var(--red-deep)"/><rect x="1" y="5" width="12" height="5" rx="1" fill="var(--red-deep)"/><rect x="3.5" y="9" width="7" height="4" fill="none" stroke="var(--red-deep)" stroke-width="1.2"/></svg>+ 000 000 000
      </li>
      <li>
        <svg viewBox="0 0 14 14"><rect x="0.5" y="3" width="13" height="8.5" fill="var(--red-deep)"/><path d="M0.5 3 L7 8 L13.5 3" fill="none" stroke="var(--white)" stroke-width="1"/></svg>info@trmigration.ca
      </li>
      <li>
        <svg viewBox="0 0 14 14"><circle cx="7" cy="7" r="6" fill="none" stroke="var(--red-deep)" stroke-width="1.4"/><ellipse cx="7" cy="7" rx="2.5" ry="6" fill="none" stroke="var(--red-deep)" stroke-width="1.1"/><line x1="1" y1="7" x2="13" y2="7" stroke="var(--red-deep)" stroke-width="1.1"/></svg>www.trmigration.ca
      </li>
    </ul>
    <div class="back-mark">T&amp;R Migration</div>
  </section>

</div>
</body>
</html>
```